North Fern Holdings Business Card

A business card design to accompany the logo design you completed on Artisan Hive. We are open to your proposals. I did add one idea below that might work, but we aren't married to the idea. The company is a real estate services company. Clientele are typically high net worth individuals, executive level employment or owners of their own company, 30-60 years old.

Our 1 (bad?) idea: double sided card; One side landscape with logo and word mark. Other side Portrait with the logo only (oversize watermark maybe?). Somewhere add text of Name (Marcus Pellington), Title (Principal), phone # (949-555-0173) and email address (marcus@northfernhq.com). There would be a second design with my wife's name, number and email in place of mine.

Again totally open to ideas here.

Industry/Entity Type

Real Estate

```html
<!DOCTYPE html>
<html lang="en">
<head>
<meta charset="utf-8">
<title>North Fern Holdings — Business Card</title>
<link href="https://fonts.googleapis.com/css2?family=Cinzel:wght@400&family=Arimo:wght@400;700&display=swap" rel="stylesheet">
<style>
  :root {
    --backdrop: #ececec;
    --card-white: #ffffff;
    --sage: #7f9d6b;
    --sage-light: #a7b898;
    --sage-deep: #6f8f5c;
    --ink-grey: #8c8c8c;
    --on-sage: #ffffff;
  }
  html, body {
    margin: 0;
    width: 1200px;
    height: 720px;
    overflow: hidden;
    background: var(--backdrop);
  }
  .canvas {
    position: relative;
    width: 1200px;
    height: 720px;
  }
  .card {
    position: absolute;
    top: 211px;
    width: 520px;
    height: 297px;
    box-sizing: border-box;
    box-shadow: 0 2px 10px rgba(0,0,0,0.10);
  }
  .card--front {
    left: 55px;
    background: var(--card-white);
  }
  .card--back {
    left: 625px;
    background: linear-gradient(160deg, var(--sage-light) 0%, var(--sage) 55%, var(--sage-deep) 100%);
  }

  /* Front side */
  .wordmark {
    font-family: "Cinzel", "Times New Roman", serif;
    font-weight: 400;
    letter-spacing: 0.04em;
    line-height: 1.05;
    margin: 0;
  }
  .card--front .wordmark {
    position: absolute;
    left: 34px;
    top: 30px;
    font-size: 30px;
    color: var(--sage);
  }
  .wordmark__line2 {
    display: block;
    padding-left: 22px;
    letter-spacing: 0.22em;
  }
  .mark-square {
    position: absolute;
    width: 58px;
    height: 58px;
  }
  .card--front .mark-square {
    right: 38px;
    top: 34px;
    background: var(--sage-light);
  }
  .contact {
    position: absolute;
    left: 34px;
    bottom: 30px;
    font-family: "Arimo", "Helvetica Neue", Arial, sans-serif;
    color: var(--ink-grey);
  }
  .contact__name {
    margin: 0;
    font-size: 20px;
    font-weight: 700;
    color: var(--sage);
    line-height: 1.1;
  }
  .contact__title {
    margin: 0 0 18px;
    font-size: 14px;
    line-height: 1.1;
  }
  .contact__line {
    margin: 0 0 14px;
    font-size: 15px;
    line-height: 1.1;
  }
  .contact__line:last-child { margin-bottom: 0; }

  /* Back side */
  .back-lockup {
    position: absolute;
    left: 0;
    right: 0;
    top: 50%;
    transform: translateY(-50%);
    display: flex;
    align-items: center;
    justify-content: center;
    gap: 26px;
  }
  .card--back .mark-square {
    position: static;
    background: var(--on-sage);
    width: 64px;
    height: 64px;
  }
  .card--back .wordmark {
    font-size: 34px;
    color: var(--on-sage);
  }
</style>
</head>
<body>
  <main class="canvas">
    <section class="card card--front" aria-label="Business card front">
      <h1 class="wordmark">North Fern<span class="wordmark__line2">Holdings</span></h1>
      <div class="mark-square" aria-hidden="true"></div>
      <div class="contact">
        <p class="contact__name">Marcus Pellington</p>
        <p class="contact__title">Principal</p>
        <p class="contact__line">marcus@northfernhq.com</p>
        <p class="contact__line">949-555-0173</p>
      </div>
    </section>

    <section class="card card--back" aria-label="Business card back">
      <div class="back-lockup">
        <div class="mark-square" aria-hidden="true"></div>
        <p class="wordmark">North Fern<span class="wordmark__line2">Holdings</span></p>
      </div>
    </section>
  </main>
</body>
</html>
```